PennacottHoldings.com Website Design

Simple website using existing logo. See "free website" already up. Want something much more professional and dynamic. Purpose is to describe my business and give me a place to post and update projects as they move along. Need to be able to post links to other companies that my firm invests equity in.
Target Market(s)
Banks, Financial Advisors
Industry/Entity Type
It Professional
Number of Pages Required
4 page
Font styles to use
Sans Serif
Requirements
Must have
- Ability to add and edit projects so they appear in the order of most current to oldest.
Nice to have
- Page to blog and link to facebook page

```html
<!DOCTYPE html>
<html lang="en">
<head>
<meta charset="utf-8">
<title>PennacottHoldings.com</title>
<link href="https://fonts.googleapis.com/css2?family=Open+Sans:wght@400;600;700;800&display=swap" rel="stylesheet">
<style>
:root{
  --red:#e0161d;
  --dark:#1c1c1e;
  --darker:#111113;
  --ink:#2a2a2a;
  --grey:#7a7a7a;
  --light:#f4f4f4;
  --white:#ffffff;
}
*{margin:0;padding:0;box-sizing:border-box}
html,body{width:723px;height:1200px;overflow:hidden;background:var(--white)}
body{font-family:"Open Sans",Arial,sans-serif;color:var(--ink);position:relative}

.site-header{position:absolute;top:0;left:0;width:723px;height:53px;background:var(--darker);display:flex;align-items:center;justify-content:space-between;padding:0 36px 0 40px}
.brand{display:flex;align-items:center;gap:8px;color:var(--white);font-weight:700;font-size:15px;letter-spacing:.3px}
.brand-square{width:20px;height:20px;background:var(--red)}
.main-nav{display:flex;gap:24px;font-size:10px;font-weight:600;color:var(--white);letter-spacing:.5px}
.main-nav a{color:inherit;text-decoration:none;padding:19px 0 16px;border-bottom:3px solid transparent}
.main-nav a.active{border-bottom-color:var(--red)}

.hero{position:absolute;top:53px;left:0;width:723px;height:309px;background:linear-gradient(135deg,#3a3a3c 0%,#1f1f21 45%,#2d2d30 70%,#141416 100%)}
.hero-title{position:absolute;left:96px;top:104px;font-size:30px;line-height:34px;font-weight:800;color:var(--white);text-transform:uppercase;letter-spacing:-.3px}
.hero-title .accent{color:var(--red)}
.hero-arrow{position:absolute;top:118px;width:26px;height:26px;border-radius:50%;display:flex;align-items:center;justify-content:center}
.hero-arrow.prev{left:30px;background:#4a4a4c}
.hero-arrow.next{right:36px;background:var(--red)}
.hero-dots{position:absolute;left:96px;top:288px;display:flex;gap:6px}
.hero-dots span{width:6px;height:6px;border-radius:50%;background:#777}
.hero-dots span.on{background:var(--red)}

.about{position:absolute;top:362px;left:0;width:723px;height:270px;background:var(--light)}
.about-photo{position:absolute;left:0;top:0;width:362px;height:270px;background:linear-gradient(160deg,#9a9ea4 0%,#6e7278 55%,#3c3f44 100%)}
.about-panel{position:absolute;left:362px;top:0;width:361px;height:270px;background:var(--white);padding:36px 40px 0 30px}
.about-kicker{font-size:20px;font-weight:800;color:var(--red);line-height:22px}
.about-title{font-size:20px;font-weight:800;color:var(--ink);line-height:24px;margin-bottom:12px}
.about-text{font-size:8.5px;line-height:13px;color:var(--grey)}
.btn{display:inline-flex;align-items:center;gap:8px;margin-top:18px;background:var(--red);color:var(--white);font-size:8px;font-weight:700;padding:6px 12px;letter-spacing:.4px}

.section-title{position:absolute;left:0;width:723px;text-align:center;font-size:21px;font-weight:800;letter-spacing:.5px;color:var(--ink)}
.section-sub{position:absolute;left:0;width:723px;text-align:center;font-size:9.5px;line-height:13px;color:var(--grey);padding:0 200px}

.projects-title{top:680px}
.projects-sub{top:716px}
.project-track{position:absolute;top:752px;left:96px;display:flex;gap:5px}
.project-card{width:174px;height:159px;position:relative}
.project-card.house-a{background:linear-gradient(180deg,#b9cfe2 0%,#c7b8a4 55%,#5f7d45 100%)}
.project-card.feature{background:linear-gradient(180deg,#3b3d40 0%,#26282b 100%);display:flex;flex-direction:column;align-items:center;padding-top:36px;text-align:center;color:var(--white)}
.project-card.house-b{background:linear-gradient(180deg,#c9dbe9 0%,#d6ccb4 55%,#8aa360 100%)}
.feature-name{font-size:13px;font-weight:700;line-height:17px;padding:0 18px}
.feature-role{font-size:8px;color:#cfcfcf;margin-top:4px}
.feature-plus{margin-top:14px;width:32px;height:32px;border-radius:50%;background:var(--red);display:flex;align-items:center;justify-content:center}
.track-arrow{position:absolute;top:820px;width:22px;height:22px;border-radius:50%;display:flex;align-items:center;justify-content:center}
.track-arrow.prev{left:60px;background:var(--red)}
.track-arrow.next{left:640px;background:#d8d8d8}

.clients-title{top:935px}
.clients-sub{top:971px}
.client-grid{position:absolute;top:1014px;left:96px;width:531px;display:grid;grid-template-columns:repeat(6,1fr);row-gap:20px;column-gap:6px}
.client{font-size:10px;font-weight:700;color:#555;text-align:center;height:20px;line-height:20px;white-space:nowrap}

.site-footer{position:absolute;bottom:0;left:0;width:723px;height:31px;background:var(--darker);display:flex;align-items:center;justify-content:space-between;padding:0 40px;color:#aaa;font-size:7.5px}
.site-footer .hl{color:var(--red)}
.social{display:flex;align-items:center;gap:6px}
.social i{width:13px;height:13px;border-radius:50%;background:var(--red);display:block}
</style>
</head>
<body>

<header class="site-header">
  <div class="brand"><span class="brand-square"></span>Pennacott Holdings</div>
  <nav class="main-nav">
    <a class="active" href="#">HOME</a><a href="#">BIO</a><a href="#">SERVICES</a><a href="#">BLOG</a><a href="#">CONTACT</a>
  </nav>
</header>

<section class="hero" role="img" aria-label="Dark photograph of a modern glass office building seen from below">
  <div class="hero-arrow prev"><svg width="8" height="8" viewBox="0 0 8 8"><path d="M5.5 1 2.5 4l3 3" stroke="#fff" stroke-width="1.5" fill="none"/></svg></div>
  <h1 class="hero-title"><span class="accent">Global real estate</span><br>markets and the<br>purchase of notes<br>and debt.</h1>
  <div class="hero-arrow next"><svg width="8" height="8" viewBox="0 0 8 8"><path d="M2.5 1l3 3-3 3" stroke="#fff" stroke-width="1.5" fill="none"/></svg></div>
  <div class="hero-dots"><span class="on"></span><span></span><span></span><span></span></div>
</section>

<section class="about">
  <div class="about-photo" role="img" aria-label="Portrait photograph of the company founder in a suit"></div>
  <div class="about-panel">
    <div class="about-kicker">ABOUT</div>
    <h2 class="about-title">PENNACOTT HOLDINGS</h2>
    <p class="about-text">Pennacott Holdings is the private equity arm of The Pennacott Group, a prominent family-owned real estate company based in Easton, Ohio. Pennacott Holdings is wholly owned by Alan Pennacott, its founder. After 20 years with the group, he remains on its board and has shifted his day-to-day work toward private investments, primarily in emerging technologies.</p>
    <a class="btn" href="#">READ MORE <svg width="6" height="7" viewBox="0 0 6 7"><path d="M1 .5 4.5 3.5 1 6.5" stroke="#fff" stroke-width="1.4" fill="none"/></svg></a>
  </div>
</section>

<h2 class="section-title projects-title">PROJECTS</h2>
<p class="section-sub projects-sub">Empower entrepreneurs to chase their dreams by providing equity capital, business consulting services, and mentoring.</p>
<div class="track-arrow prev"><svg width="7" height="7" viewBox="0 0 8 8"><path d="M5.5 1 2.5 4l3 3" stroke="#fff" stroke-width="1.5" fill="none"/></svg></div>
<div class="project-track">
  <div class="project-card house-a" role="img" aria-label="Photograph of a suburban two-storey house with lawn"></div>
  <div class="project-card feature">
    <div class="feature-name">Regional Housing Alliance</div>
    <div class="feature-role">Board of Directors</div>
    <div class="feature-plus"><svg width="12" height="12" viewBox="0 0 12 12"><path d="M6 1v10M1 6h10" stroke="#fff" stroke-width="2"/></svg></div>
  </div>
  <div class="project-card house-b" role="img" aria-label="Photograph of a row of new family homes"></div>
</div>
<div class="track-arrow next"><svg width="7" height="7" viewBox="0 0 8 8"><path d="M2.5 1l3 3-3 3" stroke="#fff" stroke-width="1.5" fill="none"/></svg></div>

<h2 class="section-title clients-title">CLIENTS</h2>
<p class="section-sub clients-sub">Empower entrepreneurs to chase their dreams by providing equity capital, business consulting services, and mentoring.</p>
<div class="client-grid">
  <div class="client">Aurelle</div><div class="client">Brevik</div><div class="client">Haiwen</div><div class="client">Rowan</div><div class="client">Bellpoint</div><div class="client">Kestrel</div>
  <div class="client">Lumara</div><div class="client">Lorvenne</div><div class="client">Peninvale</div><div class="client">Mareno</div><div class="client">Melisande</div><div class="client">Minterra</div>
  <div class="client">Valdora</div><div class="client">Quillmore</div><div class="client">Fairpath Financial</div><div class="client">Solvane</div><div class="client">Ridgeway</div><div class="client">Yarrowly</div>
</div>

<footer class="site-footer">
  <div>Copyright 2015 <span class="hl">Pennacott Holdings</span> | All Rights Reserved | Cookies &amp; Privacy</div>
  <div class="social">Find us <i></i><i></i></div>
</footer>

</body>
</html>
```